Business Card Design

I am a mental health counselor in private practice. I provide counseling to individuals, couples, and adults. There is a design on PrintHaven that I really like. It is 2 talking bubbles joined together by a heart. That is just a suggestion. I'm interested in other ideas. I would like my photo to be on the back of the card, along with the text Danielle Overby Counseling. I would like mint green as my background color and navy writing, if possible. The final design should be elegant, professional, and maybe just a touch whimsical.
Target Market(s)
Individual adolescents, adults, couples, and families seeking counseling.
Industry/Entity Type
Mental Health
Contact Information for Business Card
Danielle Overby
A Wholehearted Approach to Counseling
Danielle Overby, M.S. NCC
Marlowe Lodge
2740 NW Kestrel Avenue, Suite 215
Portland OR 97201
503-862-1157
counselingwithdanielle.example
Requirements
Must have
- The card must have all of the text provided and my photo.
Nice to have
- I like cards that are rounded on the sides, and I like thick paper.

```html
<!DOCTYPE html>
<html lang="en">
<head>
<meta charset="utf-8">
<title>Danielle Overby Counseling – Business Card</title>
<link rel="stylesheet" href="https://fonts.googleapis.com/css2?family=Open+Sans:wght@300;400&family=Quicksand:wght@400;500&display=swap">
<style>
  :root {
    --page-bg: #ecebe8;
    --card-white: #ffffff;
    --teal: #2ec4c0;
    --ink: #3d3f44;
    --ink-soft: #6d7075;
    --photo-light: #e9eaec;
    --photo-mid: #d8c9bd;
    --photo-skin: #e8b9a6;
    --photo-hair: #e6d4b0;
    --photo-dark: #2a2a2c;
    --shadow: 0 18px 40px rgba(0,0,0,0.18);
  }
  * { box-sizing: border-box; margin: 0; padding: 0; }
  html, body {
    width: 1200px; height: 1200px; overflow: hidden;
    background: var(--page-bg);
    font-family: "Quicksand", "Open Sans", sans-serif;
  }
  .sheet {
    position: relative; width: 1200px; height: 1200px;
    display: flex; justify-content: center; align-items: center; gap: 80px;
  }
  .card {
    position: relative; width: 400px; height: 700px;
    border-radius: 26px; overflow: hidden;
    background: var(--card-white); box-shadow: var(--shadow);
  }

  /* Photo side */
  .card--photo .portrait {
    position: absolute; inset: 0;
    background:
      radial-gradient(ellipse 38% 30% at 50% 52%, var(--photo-skin) 0%, var(--photo-skin) 55%, transparent 100%),
      radial-gradient(ellipse 60% 45% at 50% 50%, var(--photo-hair) 0%, var(--photo-hair) 60%, transparent 100%),
      linear-gradient(180deg, var(--photo-light) 0%, var(--photo-light) 30%, var(--photo-mid) 60%, var(--photo-dark) 88%, var(--photo-dark) 100%);
  }
  .card--photo .practice-name {
    position: absolute; top: 34px; left: 34px;
    font-family: "Open Sans", sans-serif; font-weight: 300;
    font-size: 42px; line-height: 1.08; color: var(--ink);
  }

  /* Contact side */
  .card--contact {
    display: flex; flex-direction: column;
    padding: 66px 24px 64px 34px;
  }
  .contact-header { padding-left: 86px; }
  .contact-name {
    font-size: 31px; font-weight: 400; line-height: 1.1;
    letter-spacing: 0.3px; white-space: nowrap;
  }
  .contact-name .first { color: var(--teal); }
  .contact-name .last { color: var(--ink); }
  .contact-title {
    margin-top: 6px; font-size: 15px; color: var(--ink-soft); white-space: nowrap;
  }
  .contact-list {
    margin-top: 70px; padding-left: 86px;
    list-style: none; font-size: 14px; color: var(--ink-soft); line-height: 1.5;
  }
  .contact-list li { display: flex; gap: 10px; align-items: flex-start; margin-bottom: 20px; white-space: nowrap; }
  .contact-list li.tight { margin-bottom: 6px; }
  .contact-list svg { flex: 0 0 16px; width: 16px; height: 16px; margin-top: 2px; }

  .brand { margin-top: auto; }
  .brand-mark {
    width: 58px; height: 58px; border-radius: 50%;
    background: var(--teal); margin-bottom: 16px; margin-left: 40px;
  }
  .brand-name {
    font-size: 25px; font-weight: 400; color: var(--teal); line-height: 1; white-space: nowrap;
  }
  .brand-tagline {
    margin-top: 6px; font-size: 12.5px; color: var(--ink-soft); white-space: nowrap;
  }
</style>
</head>
<body>
<main class="sheet">

  <section class="card card--photo">
    <div class="portrait" role="img" aria-label="Portrait photo of the counselor smiling, with a soft blurred office background"></div>
    <h1 class="practice-name">Danielle<br>Overby<br>Counseling</h1>
  </section>

  <section class="card card--contact">
    <header class="contact-header">
      <h2 class="contact-name"><span class="first">Danielle</span> <span class="last">Overby</span></h2>
      <p class="contact-title">Counselor Education</p>
    </header>

    <ul class="contact-list">
      <li>
        <svg viewBox="0 0 24 24" aria-hidden="true"><circle cx="12" cy="12" r="11" fill="none" stroke="#2ec4c0" stroke-width="2"/><path d="M12 5.5a4 4 0 0 0-4 4c0 3 4 8 4 8s4-5 4-8a4 4 0 0 0-4-4z" fill="#2ec4c0"/><circle cx="12" cy="9.5" r="1.5" fill="#fff"/></svg>
        <span>Marlowe Lodge<br>2740 NW Kestrel Avenue<br>Suite 215<br>Portland OR 97201</span>
      </li>
      <li class="tight">
        <svg viewBox="0 0 24 24" aria-hidden="true"><circle cx="12" cy="12" r="11" fill="none" stroke="#2ec4c0" stroke-width="2"/><path d="M8.5 6.5l2 2-1.2 1.6c.7 1.6 2 2.9 3.6 3.6l1.6-1.2 2 2-1.5 1.8c-3.8-.4-7.9-4.5-8.3-8.3z" fill="#2ec4c0"/></svg>
        <span>503-862-1157</span>
      </li>
      <li>
        <svg viewBox="0 0 24 24" aria-hidden="true"><circle cx="12" cy="12" r="11" fill="#2ec4c0"/><circle cx="12" cy="12" r="6.5" fill="none" stroke="#fff" stroke-width="1.4"/><ellipse cx="12" cy="12" rx="2.8" ry="6.5" fill="none" stroke="#fff" stroke-width="1.2"/><line x1="5.5" y1="12" x2="18.5" y2="12" stroke="#fff" stroke-width="1.2"/></svg>
        <span>counselingwithdanielle.example</span>
      </li>
    </ul>

    <div class="brand">
      <div class="brand-mark" aria-hidden="true"></div>
      <p class="brand-name">Counseling with Danielle</p>
      <p class="brand-tagline">A Wholehearted Approach to Counseling</p>
    </div>
  </section>

</main>
</body>
</html>
```